Startup Careers Fair Bunting/Banner

We'd need a bunting/banner(portrait) for an upcoming careers fair that we are going to be exhibiting at. We build innovative retail store management solutions, primarily an Vexo POS/Point of Sale on the cloud. We would like to see designs that use our primary colours of orange, black and white.

The final design should communicate a fun, exciting and attractive company to work at.

Industry/Entity Type

Retail

```html
<!DOCTYPE html>
<html lang="en">
<head>
<meta charset="utf-8">
<title>ShelfWise Careers Banner</title>
<link rel="stylesheet" href="https://fonts.googleapis.com/css2?family=Archivo:wght@800;900&family=Open+Sans:wght@400;600;700&display=swap">
<style>
  :root {
    --page: #ffffff;
    --ink: #000000;
    --white: #ffffff;
    --orange: #f08a1c;
    --orange-deep: #c8740f;
    --magenta: #8a1648;
    --smoke: #2a2a2a;
  }
  * { margin: 0; padding: 0; box-sizing: border-box; }
  html, body {
    width: 1200px; height: 433px; overflow: hidden;
    background: var(--page);
  }
  .banner {
    position: absolute; left: 14px; top: 20px;
    width: 1172px; height: 392px;
    background: var(--ink); overflow: hidden;
  }
  .banner__art { position: absolute; inset: 0; }
  .brand {
    position: absolute; left: 34px; top: 32px;
    font-family: "Open Sans", Arial, sans-serif;
  }
  .brand__row { display: flex; align-items: center; gap: 6px; }
  .brand__mark {
    width: 24px; height: 24px; background: var(--orange);
  }
  .brand__name {
    font-weight: 700; font-size: 24px; color: var(--orange);
    letter-spacing: -0.3px; line-height: 1;
  }
  .brand__tagline {
    margin-top: 9px; color: var(--white); font-size: 11px; font-weight: 400;
  }
  .pitch {
    position: absolute; left: 390px; top: 158px;
  }
  .pitch__headline {
    font-family: "Archivo", "Arial Black", sans-serif;
    font-weight: 900; color: var(--white);
    font-size: 43px; line-height: 41px; letter-spacing: -0.6px;
  }
  .pitch__services {
    margin-top: 8px;
    font-family: "Open Sans", Arial, sans-serif;
    font-size: 16px; color: var(--orange); font-weight: 400;
  }
  .pitch__dot {
    display: inline-block; width: 8px; height: 8px; border-radius: 50%;
    background: var(--white); margin: 0 4px 1px; vertical-align: middle;
  }
</style>
</head>
<body>
  <main class="banner">
    <svg class="banner__art" viewBox="0 0 1172 392" width="1172" height="392" aria-hidden="false">
      <defs>
        <radialGradient id="smokeGlow" cx="0.5" cy="0.5" r="0.5">
          <stop offset="0" stop-color="#000"/>
          <stop offset="0.6" stop-color="#111"/>
          <stop offset="0.85" stop-color="#2c2c2c"/>
          <stop offset="1" stop-color="#000" stop-opacity="0"/>
        </radialGradient>
        <linearGradient id="fadeOrange" x1="0" y1="1" x2="1" y2="0">
          <stop offset="0" stop-color="#f08a1c" stop-opacity="0.9"/>
          <stop offset="1" stop-color="#f08a1c" stop-opacity="0"/>
        </linearGradient>
        <linearGradient id="mainOrange" x1="0" y1="1" x2="1" y2="0">
          <stop offset="0" stop-color="#e0801a"/>
          <stop offset="1" stop-color="#b86f16"/>
        </linearGradient>
        <linearGradient id="magentaBand" x1="0" y1="1" x2="1" y2="0">
          <stop offset="0" stop-color="#c02a4a"/>
          <stop offset="1" stop-color="#7e1244"/>
        </linearGradient>
      </defs>
      <ellipse role="img" aria-label="Dark grey brush stroke texture swirling around the headline"
               cx="800" cy="220" rx="420" ry="260" fill="url(#smokeGlow)"/>
      <polygon class="band band--faint" points="300,0 362,0 0,330 0,268" fill="url(#fadeOrange)" opacity="0.6"/>
      <polygon class="band band--magenta" points="372,0 432,0 0,400 0,344" fill="url(#magentaBand)"/>
      <polygon class="band band--orange" points="440,0 545,0 150,392 45,392" fill="url(#mainOrange)" opacity="0.9"/>
    </svg>

    <header class="brand">
      <div class="brand__row">
        <span class="brand__mark"></span>
        <span class="brand__name">ShelfWise</span>
      </div>
      <p class="brand__tagline">Run Your Business Anywhere</p>
    </header>

    <section class="pitch">
      <h1 class="pitch__headline">We build innovative retail<br>store management solutions.</h1>
      <p class="pitch__services">Point of sale<span class="pitch__dot"></span>Inventory <span class="pitch__dot"></span> Customer relationship management</p>
    </section>
  </main>
</body>
</html>
```